Business Card & Full Stationary design For Summit Quarry
Summit Quarry For Marble & Granite
Business Card & Full Stationary design For Summit Quarry  - Construction
Creative Brief
Professional
Eng. Karim Haddouri
C.E.O
14 Shari' Nakhil el Wadi, Rawdatein, Giza, 12487, Egypt
kbh@summitquarry.com.eg
www.summitquarry.com.eg
we need everything to be included in the design ( CD, CD Cover, Letterhead, Envelopes, portfolio cover, etc..)
q7rimo q7rimo
I would highly appreciate if you can provide your concepts showing all the required stationaries including the back side of the B.Card ( Letterhead, 2 size envelope, Portfolio cover, CD, CD cover, Backgrounds for smartphones and Computers .)
Vonto Vonto

```html
<!DOCTYPE html>
<html lang="en">
<head>
<meta charset="utf-8">
<title>Summit Quarry – Business Card</title>
<link href="https://fonts.googleapis.com/css2?family=Montserrat:wght@400;600;700&display=swap" rel="stylesheet">
<style>
  :root{
    --page:#e6e5e3;
    --card:#ffffff;
    --sand:#c8b68f;
    --slate:#6e6a66;
    --ink:#2f2f2f;
    --muted:#555555;
  }
  *{margin:0;padding:0;box-sizing:border-box}
  html,body{width:1200px;height:1077px;overflow:hidden}
  body{background:var(--page);font-family:'Montserrat',sans-serif;color:var(--ink);position:relative}
  .card{position:absolute;left:170px;width:860px;height:491px;background:var(--card);box-shadow:0 6px 24px rgba(0,0,0,.12)}
  .card--front{top:40px}
  .card--back{top:546px}

  .brand{color:var(--sand);font-weight:400}
  .brand__name{font-size:64px;letter-spacing:2px;line-height:1}
  .brand__tag{font-size:16px;letter-spacing:5px;text-transform:uppercase;margin-top:16px}
  .card--front .brand{position:absolute;left:0;right:0;top:190px;text-align:center}

  .card--back .brand{position:absolute;left:60px;top:200px}
  .card--back .brand__name{font-size:40px;letter-spacing:1px}
  .card--back .brand__tag{font-size:11px;letter-spacing:4px;margin-top:10px}

  .band{position:absolute;left:0;right:0;top:340px;height:30px;background:var(--sand)}
  .band__block{position:absolute;top:0;height:30px;width:40px;background:var(--slate)}
  .band__block--one{left:60px}
  .band__block--two{left:130px}

  .info{position:absolute;right:60px;text-align:right}
  .info__title{font-size:14px;font-weight:700;letter-spacing:1px;text-transform:uppercase;margin-bottom:6px}
  .info__line{font-size:12px;color:var(--muted);line-height:1.5}
  .info--contact{top:50px}
  .info--social{top:150px}
  .person{position:absolute;right:60px;top:268px;text-align:right}
  .person__name{font-size:18px;font-weight:700;letter-spacing:1px;text-transform:uppercase}
  .person__role{font-size:12px;letter-spacing:1px;text-transform:uppercase;color:var(--muted);margin-top:4px}
</style>
</head>
<body>
  <section class="card card--front">
    <div class="brand">
      <div class="brand__name">Summit Quarry</div>
      <div class="brand__tag">Marble &amp; Granite</div>
    </div>
  </section>

  <section class="card card--back">
    <div class="brand">
      <div class="brand__name">Summit Quarry</div>
      <div class="brand__tag">Marble &amp; Granite</div>
    </div>

    <div class="info info--contact">
      <div class="info__title">Contact Us</div>
      <div class="info__line">012 555 0148</div>
      <div class="info__line">kbh@summitquarry.com.eg</div>
      <div class="info__line">www.summitquarry.com.eg</div>
    </div>

    <div class="info info--social">
      <div class="info__title">Follow Us On Social</div>
      <div class="info__line">linkpage.net/user-name</div>
      <div class="info__line">chirpline.net/user-name</div>
      <div class="info__line">folioboard.net/user-name</div>
    </div>

    <div class="person">
      <div class="person__name">John Smith</div>
      <div class="person__role">Founder</div>
    </div>

    <div class="band">
      <span class="band__block band__block--one"></span>
      <span class="band__block band__block--two"></span>
    </div>
  </section>
</body>
</html>
```